Sightless Fellowship Hall of San Diego needs an ad/flyer for convention program

Established in 1949, the Sightless Fellowship Hall of San Diego's mission is to enrich the lives of blind and visually impaired adults by preparing them for a normal, active life in a society that is principally sighted by encouraging independence.

Located in Harwick Gardens in San Diego, California, we are a nonprofit that gives blind and visually impaired people in our community an opportunity to socialize and interact. We help members build skills, confidence, and self-esteem through our various social, recreational, and educational activities. We were founded partially by Heron Guild members and receive ongoing funding from them.

We need an 8 1/2 by 11 inch color ad in jpg format. We would like it to be editable. This will be the foundation of our rebranding. The ad will be in a meeting program of the California Herons (californiaherons.example) with the goal of highlighting some of our programs in order to solicit donations from individual Heron Guilds, preferably ongoing ones.

We would like the ad to be generic enough that we can use the ad for other events and as a flyer in the future. We want the ad/flyer to be classic but eye popping with color. We want the design to reflect a professional and lively organization that loves to serve our members. We don’t entirely love our logo, but it’s what we have for now. Our next task will be a new logo design.

We would like to highlight some of our programs for our members include bingo, blind waterskiing and surfing, cooking and ceramic classes, foreign language classes, self defense classes, yoga, and craft classes. Many of the crafts our members make are sold during fundraisers, and they include blankets, scarves, beaded animals, and more. See a sampling of pictures. We provide transportation to and from our Center, free lunch while at the Center, and food to take home. Many of these activities continue during the pandemic via online platforms. We are doing monthly home deliveries of food to our members.

We need donations to keep our programs going, and we have building repairs & maintenance that we need donations in order to complete. See attached document regarding donations. Please reach out if you have questions. Thank you.

Web address: sfhsd.example
Street address: The Sightless Fellowship Hall of San Diego, 2716 Merrow St San Diego, CA 92107
Email address: donation@sfhsd.example
To make a donation: https://sfhsd.example/donate-2/

Donors

NonProfit

Sans Serif

Must have
• Highlight programs and information on how to make a donation.
Nice to have
• Information on how much each dollar donated will go - see attachment
Should not have
• Unprofessional or sloppy details

```html
<!DOCTYPE html>
<html lang="en">
<head>
<meta charset="utf-8">
<title>Sightless Fellowship Hall of San Diego – Donor Flyer</title>
<link href="https://fonts.googleapis.com/css2?family=Marcellus&family=Roboto+Condensed:wght@400;500;700&display=swap" rel="stylesheet">
<style>
  :root{
    --navy:#2e3d68;
    --navy-deep:#26345c;
    --accent:#5b78b8;
    --pill:#c9d4ee;
    --paper:#f1f1f1;
    --white:#ffffff;
    --ink:#2b3550;
    --heading:"Marcellus", Georgia, serif;
    --body:"Roboto Condensed", Arial, sans-serif;
  }
  *{box-sizing:border-box;margin:0;padding:0}
  html,body{width:938px;height:1200px;overflow:hidden;background:#e6e7e8}
  .flyer{position:relative;width:938px;height:1200px;overflow:hidden;font-family:var(--body);color:var(--white);background:var(--paper)}
  .hero-photo{position:absolute;left:0;top:0;width:938px;height:620px;
    background:linear-gradient(160deg,#3a4a72 0%,#5c6890 28%,#e89aa0 52%,#f07a6c 66%,#b28ab8 80%,#9aa0b5 100%)}
  .shapes{position:absolute;left:0;top:0}
  .brand{position:absolute;left:34px;top:40px;font-family:var(--heading);font-size:92px;color:#1c1c1c;letter-spacing:2px;line-height:1}

  .photo-circle{position:absolute;border-radius:50%;border:5px solid var(--white);box-shadow:0 0 0 4px var(--accent)}
  .angel{left:488px;top:396px;width:180px;height:180px;background:radial-gradient(circle at 50% 55%,#3c5fb8 0%,#8b9fcf 40%,#5b6170 100%)}
  .penguin{left:690px;top:382px;width:222px;height:212px;background:radial-gradient(circle at 50% 45%,#2a2a2a 0%,#8a8f98 45%,#c9ccd2 100%)}
  .teapot{left:28px;top:998px;width:150px;height:150px;background:radial-gradient(circle,#c48a4e 0%,#6b4a38 60%,#d9d3cc 100%)}
  .blanket{left:150px;top:986px;width:170px;height:170px;background:radial-gradient(circle,#f0f0f0 0%,#8d8d8d 55%,#3d3d3d 100%)}
  .flowers{left:316px;top:998px;width:150px;height:150px;background:radial-gradient(circle,#f4c9c9 0%,#e9a7b1 45%,#7f9a76 100%)}

  .pricing-title{position:absolute;left:30px;top:436px;font-family:var(--heading);font-weight:400;font-size:34px;letter-spacing:1px}
  .tier{position:absolute;left:0;width:470px}
  .tier-1{top:503px}
  .tier-2{top:619px}
  .tier-3{top:713px}
  .tier-4{top:806px}
  .tier-label{background:var(--pill);color:var(--navy);font-weight:700;font-size:15px;line-height:27px;height:27px;padding-left:34px;width:373px;border-radius:0 14px 14px 0}
  .tier ul{list-style:none;margin:8px 0 0 30px}
  .tier li{font-size:13.5px;line-height:21px}
  .tier li::before{content:"•";margin-right:9px}
  .tier-4 ul{margin-top:15px}
  .total{position:absolute;left:0;top:893px;width:480px;text-align:center}
  .total .big{font-size:21px;font-weight:500;line-height:26px}
  .total .mid{font-size:14.5px;font-weight:700;line-height:20px}
  .total .small{font-size:12.5px;opacity:.85;line-height:20px}

  .facts{position:absolute;left:530px;top:640px;width:385px;color:var(--ink)}
  .facts h2{font-family:var(--heading);font-weight:400;font-size:38px;color:var(--accent);text-align:right;letter-spacing:1px;margin-bottom:8px;line-height:46px}
  .fact{position:relative;text-align:right;font-size:13px;line-height:16.5px;padding-right:26px;margin-bottom:18px}
  .fact .hi{color:var(--accent);font-weight:700}
  .fact svg{position:absolute;right:0;top:1px}

  .donate-cta{position:absolute;left:540px;top:1022px;display:flex;align-items:center;gap:10px;color:var(--ink);font-weight:700;font-size:19px}
  .donate-url{position:absolute;left:519px;top:1100px;width:419px;height:34px;background:var(--accent);color:var(--white);font-weight:700;font-size:22px;line-height:34px;text-align:right;padding-right:30px;border-radius:17px 0 0 17px}
  .contact{position:absolute;right:32px;top:1142px;text-align:right;color:var(--ink);font-size:17px;font-weight:700;line-height:26px}
  .contact span{font-weight:500}
</style>
</head>
<body>
<main class="flyer">
  <div class="hero-photo" role="img" aria-label="Photo of a hand-knit chunky blanket in coral, purple and white draped over a chair"></div>

  <svg class="shapes" width="938" height="1200" viewBox="0 0 938 1200" aria-hidden="true">
    <defs>
      <linearGradient id="navyFade" x1="0" y1="0" x2="1" y2="0">
        <stop offset="0" stop-color="#26345c"/>
        <stop offset="1" stop-color="#5f75aa"/>
      </linearGradient>
    </defs>
    <path d="M0 0 H458 C420 120 260 170 0 190 Z" fill="#ffffff"/>
    <path d="M0 382 C180 350 420 365 700 465 L938 465 V1200 H0 Z" fill="#c9d4ee"/>
    <path d="M0 396 C180 368 420 382 700 482 L938 482 V1200 H0 Z" fill="url(#navyFade)"/>
    <path d="M482 640 C540 560 720 505 938 472 V1200 H474 C470 1000 466 800 482 640 Z" fill="#5b78b8"/>
    <path d="M494 646 C552 570 728 518 938 486 V1200 H486 C482 1000 478 802 494 646 Z" fill="#f1f1f1"/>
  </svg>

  <div class="brand">SFH</div>

  <div class="photo-circle angel" role="img" aria-label="Beaded angel craft with blue skirt"></div>
  <div class="photo-circle penguin" role="img" aria-label="Beaded penguin craft wearing a Santa hat on a knit blanket"></div>

  <h2 class="pricing-title">PRE-COVID:</h2>
  <div class="tier tier-1">
    <div class="tier-label">$10 PER MONTH OR $120 WILL BUY:</div>
    <ul>
      <li>60 meals for our lunch program – we serve 130 meals each week</li>
      <li>13 round trip CTL transportation tickets</li>
      <li>Enough beads to make 35 Nora Bell angels in our craft class</li>
    </ul>
  </div>
  <div class="tier tier-2">
    <div class="tier-label">$20 PER MONTH OR $240 WILL BUY:</div>
    <ul>
      <li>26 round trip CTL transportation tickets</li>
      <li>One month of large print and Braille translation newsletter printing</li>
    </ul>
  </div>
  <div class="tier tier-3">
    <div class="tier-label">$50 PER MONTH OR $600 WILL BUY:</div>
    <ul>
      <li>300 lunches</li>
      <li>Thanksgiving dinner with all the fixings for 80 to 100 guests</li>
    </ul>
  </div>
  <div class="tier tier-4">
    <div class="tier-label">$100 PER MONTH OR $1200 WILL BUY:</div>
    <ul>
      <li>Approximately 10 Bingo parties including food and prizes</li>
    </ul>
  </div>
  <div class="total">
    <p class="big">$1,083 PER MONTH OR $13,000 PER YEAR</p>
    <p class="mid">WILL FUND OUR ENTIRE LUNCH PROGRAM FOR THE YEAR.</p>
    <p class="small">Every dollar donated goes to support SFH participants and programs.</p>
  </div>

  <div class="photo-circle teapot" role="img" aria-label="Handmade ceramic teapot"></div>
  <div class="photo-circle blanket" role="img" aria-label="Knit blanket in grey and white with a thank-you note"></div>
  <div class="photo-circle flowers" role="img" aria-label="Pink handmade flowers"></div>

  <section class="facts">
    <h2>DID YOU KNOW?</h2>
    <p class="fact">During the pandemic we offer Bingo, Trivia and other virtual games every week, where blind and low vision participants can win SFH bucks. <span class="hi">You can sponsor one day of games for $35.</span>
      <svg width="14" height="14" viewBox="0 0 14 14"><circle cx="7" cy="7" r="6" fill="none" stroke="#5b78b8" stroke-width="1.3"/><path d="M8.3 4 5.3 7l3 3" fill="none" stroke="#5b78b8" stroke-width="1.3"/></svg></p>
    <p class="fact">You can provide 75 gift bags for our 'We are in This Together' home delivery program. Many of our blind and low vision people are isolated and stuck at home. These gift packages are welcomed with enthusiasm and gratefulness. <span class="hi">Your rewards are huge smiles and happy faces.</span>
      <svg width="14" height="14" viewBox="0 0 14 14"><circle cx="7" cy="7" r="6" fill="none" stroke="#5b78b8" stroke-width="1.3"/><path d="M8.3 4 5.3 7l3 3" fill="none" stroke="#5b78b8" stroke-width="1.3"/></svg></p>
    <p class="fact">Our building is over <span class="hi">20 years old</span> and requires<br>ongoing maintenance and repairs
      <svg width="14" height="14" viewBox="0 0 14 14"><circle cx="7" cy="7" r="6" fill="none" stroke="#5b78b8" stroke-width="1.3"/><path d="M8.3 4 5.3 7l3 3" fill="none" stroke="#5b78b8" stroke-width="1.3"/></svg></p>
    <p class="fact">Fencing (cage) required to protect outside air conditioning<br>units from vandalism. <span class="hi">Cost: $2,500</span>
      <svg width="14" height="14" viewBox="0 0 14 14"><circle cx="7" cy="7" r="6" fill="none" stroke="#5b78b8" stroke-width="1.3"/><path d="M8.3 4 5.3 7l3 3" fill="none" stroke="#5b78b8" stroke-width="1.3"/></svg></p>
    <p class="fact"><span class="hi">Wanted:</span> Sponsors for weekly virtual bingo and trivia games: Blind and Low vision participants receive one SFH buck per win. SFH bucks are turned into gift cards and CTL transportation passes. <span class="hi">Sponsor one week for $40. Sponsor 1 month for $160</span>
      <svg width="14" height="14" viewBox="0 0 14 14"><circle cx="7" cy="7" r="6" fill="none" stroke="#5b78b8" stroke-width="1.3"/><path d="M8.3 4 5.3 7l3 3" fill="none" stroke="#5b78b8" stroke-width="1.3"/></svg></p>
  </section>

  <div class="donate-cta">
    <svg width="90" height="60" viewBox="0 0 90 60" aria-hidden="true">
      <rect x="6" y="28" width="36" height="28" fill="none" stroke="#2b3550" stroke-width="2"/>
      <rect x="2" y="20" width="44" height="9" fill="none" stroke="#2b3550" stroke-width="2"/>
      <path d="M24 20v36M24 20c-5-10-15-8-11 0M24 20c5-10 15-8 11 0" fill="none" stroke="#2b3550" stroke-width="2"/>
      <path d="M86 18C78 10 66 8 56 14l4-6M56 14l7 2" fill="none" stroke="#2b3550" stroke-width="2"/>
    </svg>
    TO MAKE A DONATION:
  </div>
  <div class="donate-url">https://sfhsd.example/donate-2/</div>
  <p class="contact">donation@sfhsd.example &nbsp;|&nbsp; www.sfhsd.example<br><span>2716 Merrow St San Diego, CA 92107</span></p>
</main>
</body>
</html>
```